Ironvale Shift Services

We are a underground coal mining labour hire company, needing a website that links into our online payroll (www.wagetrakker.com.au) and also need to have job applications page that is a preform with drop down menu,s with answers or check boxes. We would also need a 3 tier administration access for access to different files.
We are looking for an ongoing relationship with future app integration

Reason: There are a few more designs to come and I'm out at the mine for another week

Industry/Entity Type

Coal Mining

```html
<!DOCTYPE html>
<html lang="en">
<head>
<meta charset="utf-8">
<title>Ironvale Shift Services</title>
<link href="https://fonts.googleapis.com/css2?family=PT+Sans:wght@400;700&display=swap" rel="stylesheet">
<style>
:root{
  --orange:#f7821f;
  --black:#0d0d0d;
  --panel:#111;
  --frame:#6b6b6b;
  --white:#ffffff;
  --text-light:#e8e8e8;
  --muted:#9a9a9a;
  --paper:#ffffff;
}
*{margin:0;padding:0;box-sizing:border-box}
html,body{width:1200px;height:1029px;overflow:hidden;background:var(--paper);font-family:"PT Sans",sans-serif}
.page{position:relative;width:1200px;height:1029px}
.hero{position:absolute;left:0;top:0;width:1200px;height:513px;
  background:linear-gradient(180deg,#9fb6c9 0%,#c7c3b4 14%,#6e5d4a 22%,#8c7a66 40%,#5c4d40 62%,#7a6350 80%,#4c3e33 100%)}
.header-frame{position:absolute;left:163px;top:0;width:876px;height:127px;background:rgba(60,60,60,.55)}
.header{position:absolute;left:171px;top:0;width:858px;height:118px;background:var(--black)}
.brand{position:absolute;left:16px;top:26px;display:flex;align-items:center;gap:10px}
.brand-dot{width:66px;height:66px;border-radius:50%;border:4px solid var(--white)}
.brand-name{font-weight:700;font-size:40px;color:var(--white);letter-spacing:1px}
.tagline{position:absolute;left:192px;top:42px;font-weight:700;font-size:10px;line-height:13px;color:var(--white);border-left:2px solid var(--orange);padding-left:10px}
.nav{position:absolute;left:292px;top:45px;display:flex;align-items:center;gap:26px;font-size:10.5px;color:var(--white)}
.nav .home{display:flex;align-items:center;gap:7px;color:var(--orange);font-weight:700}
.nav .home i{width:26px;height:26px;border-radius:50%;border:1.5px solid var(--orange);display:block}
.nav .drop::after{content:"";display:inline-block;margin-left:6px;border:3px solid transparent;border-top:4px solid #aaa;vertical-align:-2px}
.quick{position:absolute;top:387px;width:264px;height:119px;background:rgba(80,80,80,.6)}
.quick-inner{position:absolute;left:9px;top:9px;right:9px;bottom:9px;background:var(--black);display:flex;align-items:center;justify-content:center;gap:8px}
.quick-title{color:var(--orange);font-weight:700;font-size:18px;line-height:22px}
.payroll .quick-inner{background:var(--white);flex-direction:column;align-items:flex-end;padding-right:18px;gap:0}
.payroll .label{color:var(--orange);font-weight:700;font-size:17px}
.payroll .name{color:#2b2b8a;font-weight:700;font-size:36px;line-height:40px}
.welcome{position:absolute;left:0;top:513px;width:1200px;height:248px;background:#1a1a1a}
.welcome h1{position:absolute;left:206px;top:32px;width:520px;font-size:27px;line-height:35px;color:var(--orange);font-weight:700}
.welcome p{position:absolute;left:206px;top:113px;width:580px;font-size:13px;line-height:17px;color:var(--text-light)}
.checks{position:absolute;left:206px;top:178px;width:580px;display:grid;grid-template-columns:315px 265px;row-gap:10px;color:var(--orange);font-weight:700;font-size:13px}
.checks li{list-style:none;display:flex;align-items:center;gap:8px}
.checks li::before,.service-list li::before{content:"";width:13px;height:13px;border-radius:50%;border:1.5px solid #ddd;flex:none}
.mascot{position:absolute;left:797px;top:18px;width:197px;height:215px;border-radius:50%;background:radial-gradient(circle,#f7821f 0%,#7a4a22 55%,#1a1a1a 75%)}
.shadow{position:absolute;left:150px;top:761px;width:900px;height:24px;background:radial-gradient(ellipse at top,rgba(0,0,0,.18),rgba(0,0,0,0) 70%)}
.card{position:absolute;top:791px;width:264px;height:118px;background:var(--frame)}
.card-inner{position:absolute;left:9px;top:9px;right:9px;bottom:9px;background:var(--black);padding:10px 14px}
.card-inner::before{content:"";position:absolute;left:14px;top:0;border:7px solid transparent;border-top:7px solid var(--frame)}
.card h2{color:var(--orange);font-size:19px;font-weight:700;line-height:22px}
.card p,.service-list{color:var(--text-light);font-size:13px;line-height:17px;margin-top:4px}
.card .date{color:var(--muted)}
.card svg{position:absolute;right:12px;top:12px}
.service-list li{list-style:none;display:flex;gap:7px}
.more{position:absolute;right:0;bottom:0;padding:4px 12px;background:#262626;color:#ddd;font-size:12px}
.card.news .more{background:var(--orange);color:var(--white)}
.footer{position:absolute;left:174px;top:960px;font-size:13px;color:#222}
.footer-brand{position:absolute;left:956px;top:953px;display:flex;align-items:center;gap:5px;color:var(--orange);font-size:22px;font-weight:400}
.footer-brand i{width:30px;height:30px;border-radius:50%;border:2px solid var(--orange);display:block}
</style>
</head>
<body>
<div class="page">
  <div class="hero" role="img" aria-label="Photograph of two workers in hi-vis vests and hard hats overlooking an open-cut coal mine"></div>

  <div class="header-frame"></div>
  <header class="header">
    <div class="brand"><span class="brand-dot"></span><span class="brand-name">ISS</span></div>
    <div class="tagline">FLEXIBLE<br>RESOURCEFUL<br>RELIABLE</div>
    <nav class="nav">
      <span class="home"><i></i>HOME</span>
      <span>APPLICATION</span>
      <span>PAY PORTAL</span>
      <span class="drop">INFORMATION</span>
      <span>ABOUT US</span>
      <span>CONTACT</span>
      <span>MISSION</span>
    </nav>
  </header>

  <a class="quick payroll" style="left:171px">
    <div class="quick-inner"><span class="label">Our online payroll</span><span class="name">wagetrakker</span></div>
  </a>
  <a class="quick" style="left:468px">
    <div class="quick-inner">
      <svg width="72" height="56" viewBox="0 0 72 56" aria-hidden="true">
        <rect x="2" y="2" width="52" height="36" rx="2" fill="none" stroke="#f7821f" stroke-width="4"/>
        <rect x="20" y="40" width="16" height="6" fill="#f7821f"/><rect x="12" y="46" width="32" height="4" fill="#f7821f"/>
        <text x="7" y="20" font-family="PT Sans, sans-serif" font-weight="700" font-size="13" fill="#f7821f">JOB</text>
        <circle cx="52" cy="36" r="10" fill="#0d0d0d" stroke="#f7821f" stroke-width="4"/>
        <line x1="59" y1="43" x2="68" y2="52" stroke="#f7821f" stroke-width="5"/>
      </svg>
      <span class="quick-title">Our Job<br>Vacancies</span>
    </div>
  </a>
  <a class="quick" style="left:765px">
    <div class="quick-inner">
      <svg width="62" height="60" viewBox="0 0 62 60" aria-hidden="true" fill="#f7821f">
        <circle cx="12" cy="24" r="7"/><path d="M0 46a12 12 0 0 1 24 0z"/>
        <rect x="40" y="2" width="14" height="10"/><rect x="40" y="18" width="14" height="10"/>
        <rect x="40" y="34" width="14" height="10"/><rect x="40" y="50" width="14" height="10"/>
        <rect x="30" y="7" width="4" height="48"/><rect x="30" y="7" width="10" height="3"/>
        <rect x="30" y="22" width="10" height="3"/><rect x="30" y="38" width="10" height="3"/><rect x="30" y="53" width="10" height="3"/>
      </svg>
      <span class="quick-title">Employee<br>Benifit<br>Programs</span>
    </div>
  </a>

  <section class="welcome">
    <h1>WELCOME TO IRONVALE SHIFT SERVICES</h1>
    <p>we are experienced in ground consolidation in underground coal mines, in short when they collapse or cave in we come in with chemical pumps and stabilise the ground or fill cavities which will then allow for the mining process to continue. We also do general mine labor as well.</p>
    <ul class="checks">
      <li>Roadheader Drivage / Tunnel Excavation</li>
      <li>Training and Training Development</li>
      <li>Labour Hire</li>
    </ul>
    <div class="mascot" role="img" aria-label="Illustrated badge of a coal miner with pickaxe on an orange starburst"></div>
  </section>
  <div class="shadow"></div>

  <article class="card news" style="left:171px">
    <div class="card-inner">
      <h2>News</h2>
      <svg width="20" height="20" viewBox="0 0 20 20" aria-hidden="true"><rect x="3" y="5" width="14" height="9" rx="1" transform="rotate(-35 10 10)" fill="none" stroke="#f7821f" stroke-width="2"/></svg>
      <p>we are experienced in ground consolidation in underground coal mines.... <span class="date">12-12-2013</span></p>
      <span class="more">LEARN MORE</span>
    </div>
  </article>
  <article class="card" style="left:468px">
    <div class="card-inner">
      <h2>Services</h2>
      <svg width="26" height="18" viewBox="0 0 26 18" aria-hidden="true"><path d="M2 2q10 2 16 8" stroke="#f7821f" stroke-width="2.5" fill="none"/><path d="M8 17l8-8 8 8z" fill="#f7821f"/></svg>
      <ul class="service-list">
        <li>Roadheader Drivage / Tunnel Excavation</li>
        <li>Labour Hire</li>
      </ul>
      <span class="more">LEARN MORE</span>
    </div>
  </article>
  <article class="card" style="left:765px">
    <div class="card-inner">
      <h2>Engineering</h2>
      <svg width="18" height="18" viewBox="0 0 18 18" aria-hidden="true"><path d="M2 12a7 7 0 0 1 14 0h2v3H0v-3z" fill="#f7821f"/></svg>
      <p>Lorem ipsum dolor sit amet, consectetuer adipiscing elit, sed diam nonummy ...</p>
      <span class="more">LEARN MORE</span>
    </div>
  </article>

  <footer>
    <p class="footer">©2014 Ironvale Shift Services – Underground Construction – Coal Mine Services</p>
    <div class="footer-brand"><i></i>ISS</div>
  </footer>
</div>
</body>
</html>
```